Vela Errands Web Design Project

Homepage components
o Logo
o Rotating header
o Main menu
o Animation video
o Banners
o Members login
o Latest news

The design’s preferred colors are black (background), silver (main tabs) and white (text)

Site map:
• Home
• News
• About us
o Welcome Note
o Company Profile
• Member Log in
o Registered homepage
? Request a service (form)
? Services directory
? Update profile
? Services history
• Member registration
o Registration form
• Partners
Footer Menu
• Contact us
• Terms & Conditions
• Privacy policy
• Social media links
• Sitemap

Brief about the company:
Vela Errands is a Jordanian company dedicated to elevate and redefine the level of service in the country. We are set out to give premium services at affordable prices. In this fast paced environment that we live in, we barely have the luxury of free time anymore and we, at Vela Errands will be giving you that extra hour or two per day to spend as your heart desires!
By becoming a member you will get access to a world of comfort and peace of mind. We have done the homework on your behalf and have established the network of connections that will enable you to live a headache free life.
We will be providing our members with support and assistance in their day to day lives in the fields that consumes and wastes time the most. We are value driven and below is our “ever-growing” list of services that we will provide at excellent prices:
• Maintenance (carpentry, plumbing, electrical, painting, decorating, gardening… etc)
• Cleaning (pre and post tenancy, periodical deep cleaning, packing and moving services, laundry… etc)
• Personalized delivery services (grocery, important documents, office related supplies, posting cheques, food, paying bills… etc)
• Passport, driving license and ID reissuance
• Travel arrangements (flights, hotels, airport transfers… etc)
• Premium car rental services
• Restaurant reservations
• IT assistance
• Event planning and all related services
• Catering arrangements

Aside from all the services we have on offer we have collaborated with a number of places (that we like to call partners) in town where Vela Errands members are entitled to benefits and privileges that will most certainly add value to their membership. Alongside our partners we have come up with the best formula that will please our members. Below are some of our current partners:

Requirements
Must have
• Homepage components
o Logo
o Rotating header
o Main menu
o Animation video
o Banners
o Members login
o Latest news

```html
<!DOCTYPE html>
<html lang="en">
<head>
<meta charset="utf-8">
<title>Vela Errands</title>
<link href="https://fonts.googleapis.com/css2?family=Source+Sans+3:ital,wght@0,300;0,400;0,600;0,700;1,400;1,600;1,700&display=swap" rel="stylesheet">
<style>
:root{
  --black:#000;
  --white:#fff;
  --text-dark:#333;
  --muted:#8a8a8a;
  --label:#8c8c8c;
  --silver-top:#d9d9d9;
  --silver-bottom:#9c9c9c;
  --band-light:#e6e6e6;
  --band-dark:#b5b5b5;
  --field-border:#9a9a9a;
}
*{box-sizing:border-box;margin:0;padding:0}
html,body{width:1200px;height:900px;overflow:hidden;background:var(--black)}
body{position:relative;font-family:"Source Sans 3",sans-serif;color:var(--white)}
.abs{position:absolute}

.brand{left:138px;top:26px;width:340px}
.brand-name{font-size:50px;font-weight:300;color:var(--white);line-height:1;letter-spacing:1px}
.brand-tagline{margin-top:6px;margin-left:40px;font-size:16px;color:var(--muted);font-weight:400}

.login{left:675px;top:52px;width:386px;height:80px}
.login-title{position:absolute;right:2px;top:3px;font-size:14px;color:#c9c9c9;display:flex;align-items:center;gap:6px}
.login-field{position:absolute;top:30px;width:130px;height:23px;background:var(--white);border:1px solid var(--field-border);font-size:12px;color:#777;padding:3px 9px;letter-spacing:.5px}
.login-field.user{left:0}
.login-field.pass{left:142px}
.login-btn{position:absolute;left:283px;top:29px;width:102px;height:25px;border-radius:3px;background:linear-gradient(#8a8a8a,#3c3c3c);color:#eee;font-size:14px;font-weight:600;padding:3px 0 0 30px}
.login-btn span{position:absolute;right:10px;top:3px;font-size:12px;color:#bbb}
.keep{position:absolute;left:0;top:63px;font-size:11px;color:var(--muted);display:flex;align-items:center;gap:8px;letter-spacing:.4px}
.forgot{position:absolute;right:0;top:63px;font-size:11px;color:var(--white);font-weight:600;letter-spacing:.3px}

.band{left:0;top:180px;width:1200px;height:387px;background:linear-gradient(90deg,var(--band-light),#cfcfcf 30%,var(--band-dark) 100%)}

.nav{left:105px;top:148px;width:994px;height:56px;border-radius:12px 12px 0 0;background:linear-gradient(var(--silver-top),var(--silver-bottom));box-shadow:0 2px 4px rgba(0,0,0,.3)}
.nav-item{position:absolute;top:19px;font-size:15px;font-weight:600;color:var(--text-dark)}
.nav-item.active{left:35px;top:9px;width:82px;height:37px;border-radius:4px;background:linear-gradient(#fafafa,#dcdcdc);box-shadow:0 1px 3px rgba(0,0,0,.35);text-align:center;padding-top:10px}
.social{position:absolute;right:36px;top:19px;display:flex;gap:3px}
.social i{display:block;width:16px;height:16px;border-radius:3px;background:linear-gradient(#aaa,#6f6f6f)}
.social i:last-child{background:linear-gradient(#9fd6e6,#5aa7c4)}

.hero{left:105px;top:203px;width:994px;height:364px;background:
  linear-gradient(90deg,rgba(170,180,185,.95) 0%,rgba(150,160,165,.9) 45%,rgba(60,80,70,.5) 70%,rgba(90,110,90,.55) 100%),
  linear-gradient(180deg,#5b6a72 0%,#7f8c7c 45%,#a9a493 75%,#c8b49a 100%)}
.hero-copy{left:614px;top:285px;width:428px;font-style:italic}
.hero-title{font-size:29px;font-weight:700;line-height:1.1}
.hero-sub{font-size:20px;font-weight:600;margin-top:2px}
.hero-text{font-size:12px;line-height:21px;text-align:justify;margin-top:30px;font-weight:600}
.read-more{left:608px;top:457px;width:159px;height:37px;border-radius:19px;background:linear-gradient(#a4a4a4,#5e5e5e);box-shadow:0 1px 2px rgba(0,0,0,.5);font-size:18px;color:var(--white);text-align:center;padding-top:6px;font-weight:600}

.service{position:absolute;width:130px;text-align:center}
.service-label{font-size:12px;line-height:18px;color:var(--label);text-transform:uppercase;height:36px;font-weight:600;letter-spacing:.1px}
.service-thumb{position:absolute;width:103px;height:103px;background:var(--white);padding:5px}
.service-thumb div{width:100%;height:100%}

.news{left:836px;top:636px;width:230px}
.news-heading{font-size:29px;font-weight:300;letter-spacing:1px;margin-bottom:17px}
.news-date{font-size:12px;color:#bbb;line-height:21px;padding-left:3px}
.news-title{font-size:12px;font-weight:700;line-height:21px;padding-left:3px}
.news-text{font-size:12px;line-height:21px;padding-left:3px}
.news-more{font-size:12px;font-weight:700;margin:21px 0 21px;padding-left:3px}
</style>
</head>
<body>

<div class="abs brand">
  <div class="brand-name">Vela Errands</div>
  <div class="brand-tagline">we make life easier</div>
</div>

<div class="abs login">
  <div class="login-title">
    <svg width="22" height="22" viewBox="0 0 22 22"><circle cx="15" cy="7" r="5" fill="none" stroke="#bbb" stroke-width="3"/><path d="M11 11 3 19M5 17l2 2M7 15l2 2" stroke="#bbb" stroke-width="3" stroke-linecap="round"/></svg>
    Login to your account
  </div>
  <div class="login-field user">User name</div>
  <div class="login-field pass">Password</div>
  <div class="login-btn">Login<span>&gt;</span></div>
  <div class="keep">
    <svg width="12" height="12" viewBox="0 0 12 12"><rect width="12" height="12" rx="2" fill="#ddd"/><path d="M3 6l2 2 4-5" stroke="#333" stroke-width="1.6" fill="none"/></svg>
    Keep me logged in for two weeks
  </div>
  <div class="forgot">Forgot your password?</div>
</div>

<div class="abs band"></div>

<div class="abs hero" role="img" aria-label="Photo of a grey armchair with a green cushion beside a window overlooking a garden"></div>

<nav class="abs nav">
  <div class="nav-item active">Home</div>
  <div class="nav-item" style="left:138px">News</div>
  <div class="nav-item" style="left:215px">About Us</div>
  <div class="nav-item" style="left:317px">Member Login</div>
  <div class="nav-item" style="left:452px">Member Registraton</div>
  <div class="social"><i></i><i></i><i></i><i></i><i></i></div>
</nav>

<div class="abs hero-copy">
  <div class="hero-title">Convergence of Vela Errands</div>
  <div class="hero-sub">One platform for all your Life Marketing needs</div>
  <p class="hero-text">Customized, Scalable &amp; Sophisticated solution for Paid Search Marketing, Social Media Marketing &amp; Display Marketing on various Ad Exchanges. Launch campaigns globally with 80% lower operational overheads &amp; at least 30% more efficiencies</p>
</div>
<div class="abs read-more">Read More</div>

<!-- services row 1 -->
<div class="service" style="left:124px;top:639px"><div class="service-label">Maintenance</div></div>
<div class="service" style="left:254px;top:639px"><div class="service-label">Cleaning</div></div>
<div class="service" style="left:379px;top:639px"><div class="service-label">Personalized<br>Deivery Services</div></div>
<div class="service" style="left:507px;top:639px"><div class="service-label">Pasport</div></div>
<div class="service" style="left:635px;top:640px"><div class="service-label">Travel<br>Arrangements</div></div>

<div class="service-thumb" style="left:137px;top:679px"><div role="img" aria-label="Classic portrait painting" style="background:linear-gradient(#4f5a3a,#6b5a30 60%,#3a2e1a)"></div></div>
<div class="service-thumb" style="left:266px;top:679px"><div role="img" aria-label="Hand cleaning a window with a blue cloth" style="background:linear-gradient(135deg,#8fa7a8,#c9d4d0 50%,#6e8fa8)"></div></div>
<div class="service-thumb" style="left:392px;top:679px"><div role="img" aria-label="Grocery shelves full of fresh produce" style="background:linear-gradient(#7a3a22,#b2702c 40%,#6e7a2e 70%,#8a6a3a)"></div></div>
<div class="service-thumb" style="left:520px;top:679px"><div role="img" aria-label="Person holding up an identity card" style="background:linear-gradient(135deg,#9aa6ad,#d8d0c8 50%,#8e9aa4)"></div></div>
<div class="service-thumb" style="left:649px;top:679px"><div role="img" aria-label="Aerial view of a coastal town by the sea" style="background:linear-gradient(135deg,#1f5d86,#3a7fa0 50%,#a7865a 75%,#2a6a8e)"></div></div>

<!-- services row 2 -->
<div class="service" style="left:124px;top:815px"><div class="service-label">Premim Car<br>Rental Services</div></div>
<div class="service" style="left:253px;top:815px"><div class="service-label">Restaurant<br>Reservations</div></div>
<div class="service" style="left:380px;top:815px"><div class="service-label">IT<br>Assistance</div></div>
<div class="service" style="left:508px;top:815px"><div class="service-label">Event<br>Planning</div></div>
<div class="service" style="left:638px;top:816px"><div class="service-label">Catering<br>Arrangements</div></div>

<div class="service-thumb" style="left:137px;top:853px"><div role="img" aria-label="Row of parked rental cars" style="background:linear-gradient(#9aa0a6,#5c6268)"></div></div>
<div class="service-thumb" style="left:265px;top:853px"><div role="img" aria-label="Diners in a busy restaurant" style="background:linear-gradient(#7a4a26,#b07a44)"></div></div>
<div class="service-thumb" style="left:392px;top:853px"><div role="img" aria-label="Support agent with a headset" style="background:linear-gradient(#e8ece6,#9cae8a)"></div></div>
<div class="service-thumb" style="left:521px;top:853px"><div role="img" aria-label="Stage lit for an event" style="background:linear-gradient(135deg,#5a2a9a,#c04aa8 50%,#3a3ab0)"></div></div>
<div class="service-thumb" style="left:649px;top:853px"><div role="img" aria-label="Catering platter decorated with orchids" style="background:linear-gradient(135deg,#c45a8a,#e8b0c8 50%,#6a8a3a)"></div></div>

<section class="abs news">
  <h2 class="news-heading">Latest News</h2>
  <div class="news-date">10 Jun2012 | 25 comments</div>
  <div class="news-title">Strategic Consulting and more</div>
  <div class="news-text">Strategic consulting capabilities that reveal and solve operational issues .</div>
  <div class="news-more">More...</div>
  <div class="news-date">10 Jun 2012 | 25 comments</div>
  <div class="news-title">Balanced knowledge</div>
  <div class="news-text">Balanced knowledge and experience in the</div>
</section>

</body>
</html>
```